Soy Candle Labels

We sell soy candles in recycled wine bottles. The wine bottle is cut in half and filled with pure and natural soy wax and scented with essential oils.
Our product represents good use of up cycling materials for a better use. The product is all natural and eco friendly.
You can see good use of labels and branding for a company in America that does the same thing http://larkwick-tapers.example/
Trya dn keep the label uncomplicated like the above labels.
We will need an area to hand stamp the scent. Similar to the labels used on the above website.
We would prefer to use a white or off white paper label with gold or bronze printing - limit the use of colour and keep the label simple and sophisticated.
Fernlow Candle Co. is our company name. Fernlow being the predominant name and candle co. written small underneath right justified.
Die cut labels might look better than a rectangle.
Dimensions should be 90mm Wide x 90mm High
The final design should communicate a professional and quality product. But stay modern and professional. Clean, elegant and sophisticated.
Can use wording such as: Hand Poured, Premium Soy Wax, All Natural, Up cycled
Have a look at the attached image for the look and feel we are going for.
Updates
Designers are having a little bit of trouble interpreting the brief into a viable design. To assist perhaps you can look at WINE LABELS on google images. Design your label around an existing style wine label to give the canld ethe feel of being a bottle of wine. Get creative! :)
Reason: We require more designs. We havnt quite got what were looking for.
Please see brief.
Industry/Entity Type
Printing
Look and feel
Each slider illustrates characteristics of the customer's brand and the style your logo design should communicate.

```html
<!DOCTYPE html>
<html lang="en">
<head>
<meta charset="utf-8">
<title>Fernlow Candle Co. — Soy Candle Label</title>
<link rel="stylesheet" href="https://fonts.googleapis.com/css2?family=Marcellus&display=swap">
<style>
  :root {
    --paper: #ffffff;
    --bronze: #b96d2c;
    --ink: #4a4a4a;
    --ink-soft: #555555;
  }
  * { margin: 0; padding: 0; box-sizing: border-box; }
  html, body {
    width: 1200px;
    height: 1200px;
    overflow: hidden;
    background: var(--paper);
  }
  .label {
    position: relative;
    width: 1200px;
    height: 1200px;
    background: var(--paper);
    font-family: "Marcellus", serif;
    color: var(--ink);
  }
  .meta {
    position: absolute;
    top: 36px;
    font-size: 25px;
    letter-spacing: 0.5px;
    color: var(--ink);
  }
  .meta--origin { left: 68px; }
  .meta--weight { right: 68px; }

  .brand {
    position: absolute;
    right: 60px;
    top: 470px;
    text-align: right;
    color: var(--bronze);
  }
  .brand__name {
    display: block;
    font-size: 250px;
    line-height: 1;
    letter-spacing: 2px;
  }
  .brand__sub {
    display: block;
    font-size: 46px;
    line-height: 1;
    margin-top: 6px;
    letter-spacing: 1px;
  }

  .claims {
    position: absolute;
    left: 68px;
    top: 924px;
    font-size: 31px;
    letter-spacing: 0.5px;
    color: var(--ink);
    white-space: nowrap;
  }
  .claims__divider { margin: 0 14px; }

  .rule-double {
    position: absolute;
    left: 0;
    top: 984px;
    width: 691px;
    height: 10px;
    border-top: 2px solid var(--ink-soft);
    border-bottom: 2px solid var(--ink-soft);
  }

  .scent-label {
    position: absolute;
    left: 829px;
    top: 1005px;
    font-size: 30px;
    letter-spacing: 1px;
    color: var(--ink);
    transform: translate(-50%, -50%) rotate(-90deg);
    white-space: nowrap;
  }
  .scent-stamp {
    position: absolute;
    left: 857px;
    top: 854px;
    width: 302px;
    height: 302px;
  }

  .base-band {
    position: absolute;
    left: 0;
    bottom: 0;
    width: 1200px;
    height: 15px;
    background: var(--bronze);
  }
</style>
</head>
<body>
  <main class="label">
    <p class="meta meta--origin">PRODUCT OF AUSTRALIA</p>
    <p class="meta meta--weight">320 GM. PREMIUM SOY WAX</p>

    <h1 class="brand">
      <span class="brand__name">Fernlow</span>
      <span class="brand__sub">CANDLE CO.</span>
    </h1>

    <p class="claims">HAND POURED<span class="claims__divider">|</span>ALL NATURAL SOY</p>
    <div class="rule-double"></div>

    <p class="scent-label">SCENT</p>
    <svg class="scent-stamp" viewBox="0 0 302 302" aria-label="Area to hand stamp the scent">
      <circle cx="151" cy="151" r="148" fill="none" stroke="#4a4a4a" stroke-width="4"/>
    </svg>

    <div class="base-band"></div>
  </main>
</body>
</html>
```